Folded A4 flyer for design&construction company

Folded A4 flyer needed. Keywords: elegant, stylish
our website www.corvimo.ae

Industry/Entity Type

Construction

```html
<!DOCTYPE html>
<html lang="en">
<head>
<meta charset="utf-8">
<title>Corvimo folded flyer – inner spread</title>
<link href="https://fonts.googleapis.com/css2?family=Arimo:wght@400&family=Great+Vibes&display=swap" rel="stylesheet">
<style>
  :root{
    --ink:#1e1e1e;
    --gold:#a98226;
    --gold-bright:#c9a227;
    --frame:#231f20;
    --paper:#f7f3ec;
    --paper-deep:#ebe3d4;
    --canvas:#ffffff;
  }
  *{margin:0;padding:0;box-sizing:border-box}
  html,body{width:1200px;height:1200px;overflow:hidden;background:var(--canvas)}
  body{position:relative;font-family:"Arimo",Arial,sans-serif;color:var(--ink)}
  .page-label{position:absolute;top:145px;width:300px;text-align:center;font-size:40px;font-weight:400}
  .page-label--one{left:184px}
  .page-label--two{left:744px}
  .spread{position:absolute;left:0;top:0;width:1200px;height:1200px}
  .brand{position:absolute;display:flex;align-items:baseline;gap:8px;white-space:nowrap}
  .brand__name{font-size:35px;letter-spacing:0.5px;color:var(--ink)}
  .brand__division{font-family:"Great Vibes",cursive;font-size:32px;color:var(--gold-bright)}
  .services{position:absolute;list-style:none;font-size:14.5px;line-height:23.2px}
  .services li{position:relative;padding-left:23px}
  .services li::before{content:"";position:absolute;left:0;top:8px;width:8px;height:8px;border-radius:50%;background:var(--gold)}
  .services li.cont::before{display:none}
</style>
</head>
<body>
<div class="page-label page-label--one">Inner 1</div>
<div class="page-label page-label--two">Inner 2</div>

<svg class="spread" viewBox="0 0 1200 1200" xmlns="http://www.w3.org/2000/svg">
  <defs>
    <linearGradient id="paper" x1="0" y1="0" x2="1" y2="1">
      <stop offset="0" stop-color="#fbf9f4"/><stop offset=".5" stop-color="#f4efe5"/><stop offset="1" stop-color="#efe8dc"/>
    </linearGradient>
    <linearGradient id="warm-room" x1="0" y1="0" x2="1" y2="1">
      <stop offset="0" stop-color="#e9b54a"/><stop offset="1" stop-color="#c98a2a"/>
    </linearGradient>
    <linearGradient id="beige-room" x1="0" y1="0" x2="1" y2="1">
      <stop offset="0" stop-color="#d8c39c"/><stop offset="1" stop-color="#a77a4b"/>
    </linearGradient>
    <linearGradient id="white-room" x1="0" y1="0" x2="1" y2="1">
      <stop offset="0" stop-color="#e8e4de"/><stop offset="1" stop-color="#9aa0aa"/>
    </linearGradient>
    <linearGradient id="bath-room" x1="0" y1="0" x2="1" y2="1">
      <stop offset="0" stop-color="#e2b77a"/><stop offset="1" stop-color="#b78550"/>
    </linearGradient>
  </defs>

  <rect x="30" y="224" width="1131" height="732" fill="url(#paper)"/>

  <!-- top bands -->
  <polygon points="30,224 308,224 296,235 30,235" fill="var(--gold)"/>
  <polygon points="310,224 596,224 596,235 322,235" fill="var(--frame)"/>
  <polygon points="596,224 872,224 860,235 596,235" fill="var(--gold)"/>
  <polygon points="874,224 1161,224 1161,235 886,235" fill="var(--frame)"/>
  <!-- bottom bands -->
  <polygon points="30,945 296,945 308,956 30,956" fill="var(--frame)"/>
  <polygon points="322,945 596,945 596,956 310,956" fill="var(--gold)"/>
  <polygon points="596,945 860,945 872,956 596,956" fill="var(--frame)"/>
  <polygon points="886,945 1161,945 1161,956 874,956" fill="var(--gold)"/>

  <!-- dividers -->
  <line x1="63" y1="585" x2="562" y2="585" stroke="var(--gold)" stroke-width="2"/>
  <line x1="628" y1="585" x2="1126" y2="585" stroke="var(--gold)" stroke-width="2"/>

  <!-- photo frames, page one -->
  <g stroke-linejoin="miter">
    <polygon points="352,274 562,274 524,414 316,414" fill="var(--frame)"/>
    <polygon role="img" aria-label="Photo: bright interior with curved staircase and golden ceiling" points="355,283 549,283 516,406 323,406" fill="url(#warm-room)" stroke="var(--gold-bright)" stroke-width="3"/>
    <polygon points="316,421 524,421 562,562 352,562" fill="var(--frame)"/>
    <polygon role="img" aria-label="Photo: classic living room with armchairs and chandelier" points="323,429 516,429 549,553 355,553" fill="url(#beige-room)" stroke="var(--gold-bright)" stroke-width="3"/>

    <polygon points="352,614 562,614 524,754 316,754" fill="var(--frame)"/>
    <polygon role="img" aria-label="Photo: white sofa lounge with tall windows" points="355,623 549,623 516,746 323,746" fill="url(#white-room)" stroke="var(--gold-bright)" stroke-width="3"/>
    <polygon points="316,762 524,762 562,902 352,902" fill="var(--frame)"/>
    <polygon role="img" aria-label="Photo: modern lounge with fire feature and sea view" points="323,770 516,770 549,893 355,893" fill="url(#white-room)" stroke="var(--gold-bright)" stroke-width="3"/>

    <!-- photo frames, page two -->
    <polygon points="629,274 840,274 876,414 664,414" fill="var(--frame)"/>
    <polygon role="img" aria-label="Photo: elegant bedroom with sitting area" points="642,283 837,283 868,406 672,406" fill="url(#beige-room)" stroke="var(--gold-bright)" stroke-width="3"/>
    <polygon points="664,421 876,421 840,562 629,562" fill="var(--frame)"/>
    <polygon role="img" aria-label="Photo: bright living room with fireplace and plants" points="672,429 868,429 837,553 642,553" fill="url(#white-room)" stroke="var(--gold-bright)" stroke-width="3"/>

    <polygon points="629,614 840,614 876,754 664,754" fill="var(--frame)"/>
    <polygon role="img" aria-label="Photo: warm marble bathroom with tub" points="642,623 837,623 868,746 672,746" fill="url(#bath-room)" stroke="var(--gold-bright)" stroke-width="3"/>
    <polygon points="664,762 876,762 840,902 629,902" fill="var(--frame)"/>
    <polygon role="img" aria-label="Photo: bathroom with freestanding tub and glass shower" points="672,770 868,770 837,893 642,893" fill="url(#white-room)" stroke="var(--gold-bright)" stroke-width="3"/>
  </g>
</svg>

<div class="brand" style="left:63px;top:290px"><span class="brand__name">CORVIMO</span><span class="brand__division">design</span></div>
<ul class="services" style="left:86px;top:349px">
  <li>Villas Interior Design</li><li>Villas Exterior Design</li><li>Landscape Design</li>
  <li>Retail Interior Design</li><li>Office Interior Design</li><li>Hospitality Interior Design</li>
  <li>Hotel Interior Design</li><li>Hotel Exterior Design</li><li>Restaurant Interior Design</li>
</ul>

<div class="brand" style="left:63px;top:638px"><span class="brand__name">CORVIMO</span><span class="brand__division">landscaping</span></div>
<ul class="services" style="left:86px;top:698px">
  <li>Soft Landscaping</li><li>Irrigation Solutions</li><li>Hard land Scaping</li>
  <li>External Lighting</li><li>Swimming Pool &amp;</li><li class="cont">Water Features</li>
</ul>

<div class="brand" style="left:876px;top:290px"><span class="brand__name">CORVIMO</span><span class="brand__division">fitout</span></div>
<ul class="services" style="left:895px;top:349px">
  <li>Development Approvals</li><li>Flooring Solutions</li><li>Partition</li>
  <li>Sealing Solutions</li><li>MEP Works</li><li>Civil Works</li>
  <li>Joinery</li><li>Glass and Aluminium Works</li><li class="cont">(subcontractor)</li>
</ul>

<div class="brand" style="left:876px;top:638px"><span class="brand__name">CORVIMO</span><span class="brand__division">maintaince</span></div>
<ul class="services" style="left:895px;top:698px">
  <li>AC Repair</li><li>Plumber Services</li><li>Electric Repair</li>
  <li>Carpentry Work</li><li>Gypsum Ceiling</li><li>Painting Services</li>
  <li>Cleaning Services</li><li>Emergency Services</li>
</ul>
</body>
</html>
```